New exciting tequila brand needs fun and attention drawing bottle label.

We need a design for on the glass bottle for a new tequila brand called "Comet Spin Tequila". It can be a label, or the decoration for the entire bottle.
The brand is called "Comet Spin" and is targeting a young party crowd.
I would like the visual to play with the image of a "tiger" & the idea of "up"side down.
In a bar the bottle needs to stand out, so it can be a very colourful design.

Good luck

Target Market(s)

young party crowd

Industry/Entity Type

Crowd

Colors
ec2027
fbed22
f37123
ffffff
f8ba93
fbf289

Requirements
Must have
• tiger
Nice to have
• play with the idea of upside down
Should not have
• have seen it before feeling

```html
<!DOCTYPE html>
<html lang="en">
<head>
<meta charset="utf-8">
<title>Comet Spin Tequila – label colourways</title>
<link href="https://fonts.googleapis.com/css2?family=Anton&family=Indie+Flower&display=swap" rel="stylesheet">
<style>
  :root {
    --paper: #ffffff;
    --ink: #1c1a1a;
    --red: #d51f2b;
    --yellow: #f6c700;
    --lemon: #fbe800;
    --amber: #f5a400;
    --orange: #ea6a1e;
    --deep-orange: #e0600f;
    --purple: #74298f;
    --teal: #17998a;
    --lime: #c6d400;
    --white: #ffffff;
  }
  * { box-sizing: border-box; margin: 0; padding: 0; }
  html, body { width: 1200px; height: 800px; overflow: hidden; background: var(--paper); }
  .sheet {
    position: relative;
    width: 1200px; height: 800px;
    display: grid;
    grid-template-columns: repeat(6, 200px);
    grid-template-rows: 400px 400px;
  }
  .variant {
    position: relative;
    display: flex; flex-direction: column; align-items: center;
  }
  .variant.top { justify-content: flex-start; padding-top: 37px; }
  .variant.bottom { justify-content: flex-end; padding-bottom: 37px; }
  .variant-number {
    font-family: "Indie Flower", cursive;
    font-size: 22px; color: var(--ink); line-height: 1;
  }
  .variant.top .variant-number { margin-bottom: 68px; }
  .variant.bottom .variant-number { margin-top: 66px; }
  .label {
    width: 122px; height: 222px;
    border: 6px solid var(--frame);
    border-radius: 10px;
    background: var(--ground);
    display: flex; flex-direction: column;
    overflow: hidden;
  }
  .label.inverted { flex-direction: column; }
  .label.upright { flex-direction: column-reverse; }
  .tiger-art {
    height: 94px; margin: 6px 8px 0;
    border-radius: 4px;
    background: linear-gradient(160deg, var(--art) 0%, var(--ground) 100%);
    opacity: .85;
  }
  .label.upright .tiger-art { margin: 0 8px 6px; background: linear-gradient(340deg, var(--art) 0%, var(--ground) 100%); }
  .wordmark {
    flex: 1;
    display: flex; flex-direction: column; align-items: center; justify-content: center;
    font-family: "Anton", sans-serif;
    font-weight: 400;
    color: var(--word);
    text-transform: uppercase;
    line-height: .92;
  }
  .label.inverted .wordmark { transform: rotate(180deg); }
  .wordmark .name { font-size: 36px; letter-spacing: .5px; }
  .wordmark .kind { font-size: 9px; letter-spacing: 3px; margin-bottom: 2px; }

  .v13 { --frame: var(--red); --ground: var(--yellow); --art: var(--teal); --word: var(--teal); }
  .v14 { --frame: #f39200; --ground: var(--amber); --art: var(--ink); --word: var(--deep-orange); }
  .v15 { --frame: var(--white); --ground: var(--purple); --art: var(--white); --word: var(--white); }
  .v15 { box-shadow: 0 0 0 1px #e4e4e4; }
  .v16 { --frame: var(--yellow); --ground: var(--teal); --art: var(--yellow); --word: var(--white); }
  .v17 { --frame: var(--ink); --ground: var(--lime); --art: var(--ink); --word: var(--red); }
  .v18 { --frame: var(--purple); --ground: var(--lemon); --art: var(--purple); --word: var(--purple); }
  .v19 { --frame: var(--orange); --ground: var(--white); --art: var(--orange); --word: var(--ink); }
  .v20 { --frame: var(--ink); --ground: var(--orange); --art: var(--ink); --word: var(--ink); }
  .v21 { --frame: var(--ink); --ground: var(--white); --art: var(--ink); --word: var(--orange); }
  .v22 { --frame: var(--orange); --ground: var(--ink); --art: var(--white); --word: var(--orange); }
  .v23 { --frame: var(--ink); --ground: var(--orange); --art: var(--white); --word: var(--ink); }
  .v24 { --frame: var(--ink); --ground: var(--orange); --art: var(--ink); --word: var(--white); }
</style>
</head>
<body>
<main class="sheet">
  <section class="variant top"><span class="variant-number">13</span>
    <div class="label inverted v13"><div class="tiger-art" role="img" aria-label="Leaping tiger illustration in teal"></div>
      <div class="wordmark"><span class="kind">Tequila</span><span class="name">Comet</span><span class="name">Spin</span></div></div></section>
  <section class="variant top"><span class="variant-number">14</span>
    <div class="label inverted v14"><div class="tiger-art" role="img" aria-label="Leaping tiger illustration in black"></div>
      <div class="wordmark"><span class="kind">Tequila</span><span class="name">Comet</span><span class="name">Spin</span></div></div></section>
  <section class="variant top"><span class="variant-number">15</span>
    <div class="label inverted v15"><div class="tiger-art" role="img" aria-label="Leaping tiger illustration in white"></div>
      <div class="wordmark"><span class="kind">Tequila</span><span class="name">Comet</span><span class="name">Spin</span></div></div></section>
  <section class="variant top"><span class="variant-number">16</span>
    <div class="label inverted v16"><div class="tiger-art" role="img" aria-label="Leaping tiger illustration in yellow"></div>
      <div class="wordmark"><span class="kind">Tequila</span><span class="name">Comet</span><span class="name">Spin</span></div></div></section>
  <section class="variant top"><span class="variant-number">17</span>
    <div class="label upright v17"><div class="tiger-art" role="img" aria-label="Upside-down tiger illustration in black"></div>
      <div class="wordmark"><span class="kind">Tequila</span><span class="name">Comet</span><span class="name">Spin</span></div></div></section>
  <section class="variant top"><span class="variant-number">18</span>
    <div class="label upright v18"><div class="tiger-art" role="img" aria-label="Upside-down tiger illustration in purple"></div>
      <div class="wordmark"><span class="kind">Tequila</span><span class="name">Comet</span><span class="name">Spin</span></div></div></section>

  <section class="variant bottom">
    <div class="label inverted v19"><div class="tiger-art" role="img" aria-label="Leaping tiger illustration in orange"></div>
      <div class="wordmark"><span class="kind">Tequila</span><span class="name">Comet</span><span class="name">Spin</span></div></div>
    <span class="variant-number">19</span></section>
  <section class="variant bottom">
    <div class="label inverted v20"><div class="tiger-art" role="img" aria-label="Leaping tiger illustration in black"></div>
      <div class="wordmark"><span class="kind">Tequila</span><span class="name">Comet</span><span class="name">Spin</span></div></div>
    <span class="variant-number">20</span></section>
  <section class="variant bottom">
    <div class="label inverted v21"><div class="tiger-art" role="img" aria-label="Leaping tiger illustration in black"></div>
      <div class="wordmark"><span class="kind">Tequila</span><span class="name">Comet</span><span class="name">Spin</span></div></div>
    <span class="variant-number">21</span></section>
  <section class="variant bottom">
    <div class="label upright v22"><div class="tiger-art" role="img" aria-label="Upside-down tiger illustration in white"></div>
      <div class="wordmark"><span class="kind">Tequila</span><span class="name">Comet</span><span class="name">Spin</span></div></div>
    <span class="variant-number">22</span></section>
  <section class="variant bottom">
    <div class="label upright v23"><div class="tiger-art" role="img" aria-label="Upside-down tiger illustration in white"></div>
      <div class="wordmark"><span class="kind">Tequila</span><span class="name">Comet</span><span class="name">Spin</span></div></div>
    <span class="variant-number">23</span></section>
  <section class="variant bottom">
    <div class="label upright v24"><div class="tiger-art" role="img" aria-label="Upside-down tiger illustration in black"></div>
      <div class="wordmark"><span class="kind">Tequila</span><span class="name">Comet</span><span class="name">Spin</span></div></div>
    <span class="variant-number">24</span></section>
</main>
</body>
</html>
```